Basic Web Design and coding (wordpress ideally). Needed live by 10th Feb!

Hi,

We are a Financial Wellness company that provides free seminars to help educate the general public and guide them to becoming debt free and prosperous.

Our company provides insurance, mortgage/ home loan and investment advice.

We require a fairly basic website that shouldn't require more then just a few pages.

The key elements to the site are as follows;

1: clean and easy to use (both on the front and back end). Clean calls to action and easy to use.

2: 4 "buttons" on the home page for the customer to choose which service they require from us which leads to a data capture form.

3: A (live?) calendar that shows all the seminars we provide across the country (location, date, time, etc) and also allows customers to register their attendance via the website. No payment is taken, just data capture. - this doesn't have to be live as long as it can be updated as needed.

4: Vorlix analytic

5: Responsive (phone, tablet etc)

Other than that its just Home, About Us, Services, Contact etc.

We already have the logo and color scheme (blue, green, white and black).

Here are a couple of templates that we like the design of - please note the position of the 4 "tabs/buttons" as these need to be seen on the home screen.

1) http://www.layoutquarry.com/demo/52036.html

2) http://www.layoutquarry.com/demo/45686.html

I will be choosing a design/contractor before the job closes.

Thank you.

Industry/Entity Type

Education

Number of Pages Required

5+ page

Requirements
Must have
• Coding. Brand continuity (color scheme), 4 buttons on the home screen, calendar.

```html
<!DOCTYPE html>
<html lang="en">
<head>
<meta charset="utf-8">
<title>The Brightledger Group</title>
<link href="https://fonts.googleapis.com/css2?family=Cinzel:wght@400;600&family=Lato:ital,wght@0,400;0,700;1,400&display=swap" rel="stylesheet">
<style>
:root{
  --green:#2f9e74;
  --green-dark:#268a64;
  --blue:#1f4e96;
  --navy:#1d3a6e;
  --ink:#2b2b2b;
  --text:#444;
  --muted:#777;
  --line:#cfcfcf;
  --paper:#ffffff;
  --gray:#ececec;
  --footer:#3b3b3b;
  --footer-bottom:#262626;
}
*{box-sizing:border-box;margin:0;padding:0}
html,body{width:1200px;height:2264px;overflow:hidden}
body{position:relative;font-family:"Lato",sans-serif;color:var(--text);background:var(--paper)}
.abs{position:absolute}
.serif{font-family:"Cinzel",serif}

/* header */
.topbar{left:0;top:0;width:1200px;height:42px;background:var(--navy)}
.topbar .welcome{left:294px;top:13px;font-size:13px;color:#dfe6f2}
.topbar .phone{right:97px;top:11px;font-size:15px;color:#fff;display:flex;align-items:center;gap:8px}
.brand-box{left:97px;top:0;width:187px;height:118px;background:#fff;display:flex;align-items:center;justify-content:center;gap:8px;z-index:2}
.brand-box .dot{width:14px;height:14px;border-radius:50%;background:var(--green)}
.brand-name{font-family:"Cinzel",serif;font-weight:600;font-size:19px;color:var(--blue);line-height:1.1;text-align:center}
.navbar{left:0;top:42px;width:1200px;height:76px;background:#fff;border-bottom:2px solid var(--navy)}
.nav{right:97px;top:24px;display:flex;align-items:center;font-family:"Cinzel",serif;font-size:17px;color:var(--ink)}
.nav a{color:inherit;text-decoration:none;padding:0 32px;border-left:1px solid #ccc;position:relative}
.nav a:first-child{border-left:none}
.nav a:last-child{padding-right:0}
.nav a.active{color:var(--green)}
.nav a.active::after{content:"";position:absolute;left:32px;right:32px;bottom:-14px;height:3px;background:var(--green)}

/* hero */
.hero{left:0;top:118px;width:1200px;height:428px}
.hero-title{left:767px;top:250px;font-family:"Cinzel",serif;font-size:25px;line-height:36px;color:#fff;letter-spacing:.5px}
.btn{display:inline-flex;align-items:center;gap:10px;color:#fff;font-size:13px;font-weight:700;border-radius:3px}
.hero-btn{left:770px;top:379px;width:137px;height:36px;background:var(--blue);padding-left:12px;font-weight:400}
.circle-arrow{width:13px;height:13px;border-radius:50%;background:#fff;display:inline-block;position:relative}
.circle-arrow::after{content:"";position:absolute;left:4px;top:3.5px;border-left:5px solid var(--blue);border-top:3px solid transparent;border-bottom:3px solid transparent}
.hero-knob{left:578px;top:524px;width:44px;height:44px;border-radius:50%;background:#fff;display:flex;align-items:center;justify-content:center}
.hero-knob span{width:10px;height:10px;border-radius:50%;background:#bbb}

/* section titles */
.sec-title{width:1200px;left:0;text-align:center;font-family:"Cinzel",serif;font-size:32px;color:var(--ink)}
.sec-title .b{color:var(--blue)}
.sec-title .g{color:var(--green)}
.divider{left:425px;width:350px;height:14px}
.divider::before,.divider::after{content:"";position:absolute;top:6px;width:155px;height:3px;border-top:1px solid #bbb;border-bottom:1px solid #bbb}
.divider::before{left:0}
.divider::after{right:0}
.divider i{position:absolute;left:168px;top:0;width:14px;height:14px;border-radius:50%;border:2px solid #999}
.on-green .divider::before,.on-green .divider::after{border-color:rgba(255,255,255,.7)}
.on-green .divider i{border-color:#fff}

.about-text{left:110px;width:980px;top:692px;text-align:center;font-size:13px;line-height:20px;color:#333}

/* services */
.services{left:0;top:812px;width:1200px;height:442px;background:var(--green)}
.services .sec-title{color:#fff;top:48px}
.services .divider{top:88px}
.services .lead{left:0;width:1200px;top:130px;text-align:center;color:#fff;font-size:13.5px}
.card{top:179px;width:235px;height:218px;background:#fff;text-align:center}
.card .icon{position:absolute;left:88px;top:12px;width:60px;height:60px;border-radius:50%;border:3px solid var(--green);display:flex;align-items:center;justify-content:center}
.card .icon span{width:48px;height:48px;border-radius:50%;background:var(--blue)}
.card h3{position:absolute;left:0;width:100%;top:108px;font-family:"Cinzel",serif;font-weight:400;font-size:17px;color:var(--ink);letter-spacing:.5px}
.card p{position:absolute;left:14px;right:14px;top:133px;font-size:13.5px;line-height:19px;color:#333}
.card .more{position:absolute;left:106px;bottom:-4px;width:24px;height:17px;background:var(--green);color:#fff;font-size:16px;line-height:16px;font-weight:700}

/* events */
.events-title{top:1290px}
.arrow{top:1460px;width:22px;height:24px}
.event{top:1403px;width:490px;height:162px;border:1px solid #ddd;background:#fff}
.event .photo{position:absolute;left:6px;top:6px;width:160px;height:151px;background:linear-gradient(135deg,#d8dde3,#8a97a6 55%,#3d4a5c)}
.event h4{position:absolute;left:181px;top:14px;font-weight:400;font-size:15px;color:#222}
.event p{position:absolute;left:181px;right:16px;top:40px;font-size:13.5px;line-height:19px;color:#444}
.event .meta{position:absolute;left:181px;top:110px;font-size:11px;color:#666;display:flex;gap:14px;align-items:center}
.event .meta span{display:inline-flex;align-items:center;gap:5px}
.event .corner{position:absolute;right:0;bottom:0;width:0;height:0;border-left:30px solid transparent;border-bottom:30px solid var(--blue)}
.event .corner-plus{position:absolute;right:4px;bottom:1px;color:#fff;font-size:15px;font-weight:700}

/* testimonials + contact */
.band{left:0;top:1610px;width:1200px;height:382px;background:var(--gray)}
.band-title{font-family:"Cinzel",serif;font-size:30px;color:var(--ink)}
.band-title .b{color:var(--blue)}
.mini-div{width:460px;height:12px}
.mini-div i{position:absolute;left:4px;top:0;width:12px;height:12px;border-radius:50%;border:2px solid #888}
.mini-div::after{content:"";position:absolute;left:24px;right:0;top:5px;border-top:1px solid #bbb}
.avatar{left:99px;top:1748px;width:88px;height:88px;border-radius:50%;background:linear-gradient(135deg,#e6e6e6,#9aa3ad);border:3px solid #fff;box-shadow:0 0 0 1px #ccc}
.quote-name{left:209px;top:1760px;font-size:17px;color:#333}
.quote-role{left:209px;top:1788px;font-size:12px;color:#555}
.quote{left:98px;top:1855px;width:462px;font-size:13.5px;line-height:19px;color:#555}
.dots{left:98px;top:1946px;display:flex;gap:6px}
.dots span{width:10px;height:10px;border-radius:50%;background:#555}
.dots span.on{background:var(--green)}
.field{background:#fff;border:1px solid #ddd;font-size:12.5px;color:#555;padding:9px 8px}
.submit{left:637px;top:1894px;width:137px;height:36px;background:var(--green);padding-left:13px}
.submit .circle-arrow::after{border-left-color:var(--green)}

/* footer */
.footer{left:0;top:1992px;width:1200px;height:229px;background:var(--footer)}
.footer h5{position:absolute;font-family:"Cinzel",serif;font-weight:400;font-size:18px;color:#fff;top:36px;padding-bottom:6px;border-bottom:1px dashed #888}
.footer .col-line{position:absolute;top:36px;width:1px;height:160px;background:#4c4c4c}
.footer ul{position:absolute;list-style:none;font-size:12px;color:#ddd;line-height:22px;top:86px}
.footer ul li::before{content:"»";margin-right:9px;color:#aaa}
.contact-line{position:absolute;display:flex;gap:12px;font-size:12px;color:#ddd;line-height:16px}
.contact-line svg{flex:none}
.news-text{position:absolute;left:625px;top:82px;width:230px;font-size:12px;line-height:17px;color:#ddd}
.news-input{position:absolute;left:625px;top:123px;width:223px;height:28px;background:#fff;border-radius:2px;font-size:12px;font-style:italic;color:#777;padding:7px 8px}
.news-btn{position:absolute;left:625px;top:162px;width:90px;height:27px;background:var(--blue);color:#fff;font-size:12px;font-weight:700;text-align:center;line-height:27px}
.foot-brand{position:absolute;left:940px;top:60px;width:180px;text-align:center;font-family:"Cinzel",serif;font-weight:600;font-size:24px;color:#cfcfcf}
.social{position:absolute;left:950px;top:173px;display:flex;gap:11px}
.social span{width:24px;height:24px;border-radius:50%;background:#6a6a6a}
.copyright{left:0;top:2221px;width:1200px;height:43px;background:var(--footer-bottom);color:#ddd;font-size:12px;text-align:center;line-height:43px}
</style>
</head>
<body>

<header>
  <div class="abs topbar">
    <div class="abs welcome">Welcome To The Brightledger Group</div>
    <div class="abs phone">
      <svg width="15" height="15" viewBox="0 0 24 24" aria-hidden="true"><path fill="#fff" d="M6.6 10.8a15.1 15.1 0 0 0 6.6 6.6l2.2-2.2a1 1 0 0 1 1-.25 11.4 11.4 0 0 0 3.6.57 1 1 0 0 1 1 1V20a1 1 0 0 1-1 1A17 17 0 0 1 3 4a1 1 0 0 1 1-1h3.5a1 1 0 0 1 1 1c0 1.25.2 2.45.57 3.57a1 1 0 0 1-.25 1z"/></svg>
      +12 - 555 - 010203
    </div>
  </div>
  <div class="abs brand-box"><span class="dot"></span><div class="brand-name">The<br>Brightledger<br>Group</div></div>
  <div class="abs navbar">
    <nav class="abs nav">
      <a class="active">Home</a><a>About Us</a><a>Services</a><a>Contact Us</a>
    </nav>
  </div>
</header>

<section class="abs hero">
  <svg width="1200" height="428" viewBox="0 0 1200 428" role="img" aria-label="Photo of a small model house resting on stacked coins, with a green panel for the headline">
    <defs>
      <linearGradient id="photoTone" x1="0" y1="0" x2="1" y2="1">
        <stop offset="0" stop-color="#9fb4c6"/>
        <stop offset=".45" stop-color="#dfe3e6"/>
        <stop offset=".7" stop-color="#c9a66a"/>
        <stop offset="1" stop-color="#8d7a5c"/>
      </linearGradient>
    </defs>
    <rect width="1200" height="428" fill="#3aa57c"/>
    <path d="M0 0 H700 C770 40 760 120 700 200 C640 290 640 360 680 428 H0 Z" fill="url(#photoTone)"/>
    <path d="M700 0 C770 40 760 120 700 200 C640 290 640 360 680 428" fill="none" stroke="#fff" stroke-width="22"/>
  </svg>
</section>
<h1 class="abs hero-title">We help to people<br>becoming debt free<br>and prosperous.</h1>
<a class="abs btn hero-btn">Contact Now <span class="circle-arrow"></span></a>
<div class="abs hero-knob"><span></span></div>

<section>
  <h2 class="abs sec-title" style="top:590px">About <span class="b">The Brightledger</span> <span class="g">Group</span></h2>
  <div class="abs divider" style="top:647px"><i></i></div>
  <p class="abs about-text">Lorem Ipsum is simply dummy text of the printing and typesetting industry. Lorem Ipsum has been the industry's standard dummy text ever since the 1500s, when an unknown printer took a galley of type and scrambled it to make a type specimen book. It has survived not only five centuries, but also the leap into electronic typesetting, remaining essentially unchanged. It was popularised in the 1960s with the release of Letraset sheets containing Lorem Ipsum passages, and more recently with desktop publishing software like Aldus PageMaker including versions of Lorem Ipsum. [...]</p>
</section>

<section class="abs services on-green">
  <h2 class="abs sec-title">Our Services</h2>
  <div class="abs divider"><i></i></div>
  <p class="abs lead">There are many variations of passages of Lorem Ipsum available, but the majority have suffered alteration in some form, by injected humour, or randomised words</p>
  <div class="abs card" style="left:97px"><div class="icon"><span></span></div><h3>Insurance</h3><p>Contrary to popular belief, Lorem Ipsum is not simply random text. It has roots in...</p><div class="more">+</div></div>
  <div class="abs card" style="left:353px"><div class="icon"><span></span></div><h3>Mortgage</h3><p>Contrary to popular belief, Lorem Ipsum is not simply random text. It has roots in a piece ...</p><div class="more">+</div></div>
  <div class="abs card" style="left:610px"><div class="icon"><span></span></div><h3>Home Loan</h3><p>Contrary to popular belief, Lorem Ipsum is not simply random text. It has roots in a piece of....</p><div class="more">+</div></div>
  <div class="abs card" style="left:866px"><div class="icon"><span></span></div><h3>Investment Advice</h3><p>Lorem Ipsum is simply dummy text of the printing and typesetting industry.....</p><div class="more">+</div></div>
</section>

<section>
  <h2 class="abs sec-title events-title">Event <span class="b">calendar</span></h2>
  <div class="abs divider" style="top:1345px"><i></i></div>
  <svg class="abs arrow" style="left:52px" viewBox="0 0 22 24" aria-hidden="true"><path d="M20 8 H10 V2 L2 12 L10 22 V16 H20 Z" fill="#fff" stroke="#555" stroke-width="1.5"/></svg>
  <svg class="abs arrow" style="left:1124px" viewBox="0 0 22 24" aria-hidden="true"><path d="M2 8 H12 V2 L20 12 L12 22 V16 H2 Z" fill="#fff" stroke="#555" stroke-width="1.5"/></svg>

  <article class="abs event" style="left:98px">
    <div class="photo" role="img" aria-label="Photo of two men shaking hands in an office"></div>
    <h4>Lorem Ipsum is simply dummy text of</h4>
    <p>It is a long established fact that a reader will be distracted by the readable content of a page when looking at its layout. The point of using</p>
    <div class="meta"><span>&#9633; 11:25 PM - 03 Feb ,16</span><span>&#9679; Lorem Ipsum</span></div>
    <div class="corner"></div><div class="corner-plus">+</div>
  </article>
  <article class="abs event" style="left:613px">
    <div class="photo" role="img" aria-label="Photo of a businessman smiling at a meeting table"></div>
    <h4>Lorem Ipsum is simply dummy text of</h4>
    <p>It is a long established fact that a reader will be distracted by the readable content of a page when looking at its layout. The point of using</p>
    <div class="meta"><span>&#9633; 11:25 PM - 03 Feb ,16</span><span>&#9679; Lorem Ipsum</span></div>
    <div class="corner"></div><div class="corner-plus">+</div>
  </article>
</section>

<section class="abs band"></section>
<h2 class="abs band-title" style="left:97px;top:1644px">Our <span class="b">People Say</span></h2>
<div class="abs mini-div" style="left:97px;top:1695px"><i></i></div>
<div class="abs avatar" role="img" aria-label="Portrait photo of a client"></div>
<div class="abs quote-name">Fundwise is Great Firm</div>
<div class="abs quote-role">Lorem Ipsum is</div>
<p class="abs quote">Neque porro quisquam est, qui dolorem ipsum quia dolor sit amet, consectetur, adipis civelit sed quia non qui dolorem ipsum quia dolor sit amet, consectetur, adipis civelit sed quia numquam eius modi. Neque porro quisquam est, qui dolorem ipsum</p>
<div class="abs dots"><span></span><span></span><span class="on"></span><span></span></div>

<h2 class="abs band-title" style="left:628px;top:1644px">Get In <span class="b">Touch</span></h2>
<div class="abs mini-div" style="left:628px;top:1695px;width:476px"><i></i></div>
<div class="abs field" style="left:637px;top:1731px;width:231px;height:34px">Your Name</div>
<div class="abs field" style="left:874px;top:1731px;width:228px;height:34px">Your Email</div>
<div class="abs field" style="left:637px;top:1772px;width:465px;height:34px">Phone Number</div>
<div class="abs field" style="left:637px;top:1813px;width:465px;height:68px">Message</div>
<a class="abs btn submit">SUBMIT NOW <span class="circle-arrow"></span></a>

<footer class="abs footer">
  <h5 style="left:97px;width:143px">Quick Links</h5>
  <ul style="left:101px"><li>Home</li><li>About Us</li><li>Services</li><li>Contact Us</li></ul>
  <div class="col-line" style="left:277px"></div>

  <h5 style="left:321px;width:208px">Contact Details</h5>
  <div class="contact-line" style="left:323px;top:83px">
    <svg width="14" height="18" viewBox="0 0 14 18" aria-hidden="true"><path d="M7 0a7 7 0 0 1 7 7c0 5-7 11-7 11S0 12 0 7a7 7 0 0 1 7-7z" fill="#fff"/><circle cx="7" cy="7" r="2.5" fill="#3b3b3b"/></svg>
    <span>Lorem ipsum dolor consectetuer<br>adipiscing elit, sed di nonummy<br>nibh euismod tincidunt.</span>
  </div>
  <div class="contact-line" style="left:323px;top:150px">
    <svg width="14" height="14" viewBox="0 0 24 24" aria-hidden="true"><path fill="#fff" d="M6.6 10.8a15.1 15.1 0 0 0 6.6 6.6l2.2-2.2a1 1 0 0 1 1-.25 11.4 11.4 0 0 0 3.6.57 1 1 0 0 1 1 1V20a1 1 0 0 1-1 1A17 17 0 0 1 3 4a1 1 0 0 1 1-1h3.5a1 1 0 0 1 1 1c0 1.25.2 2.45.57 3.57a1 1 0 0 1-.25 1z"/></svg>
    <span>+12 - 555 - 010203</span>
  </div>
  <div class="contact-line" style="left:323px;top:180px">
    <svg width="16" height="12" viewBox="0 0 16 12" aria-hidden="true"><rect width="16" height="12" fill="#fff"/><path d="M0 0 L8 7 L16 0" fill="none" stroke="#3b3b3b" stroke-width="1.5"/></svg>
    <span>hello@brightledgergroup.com</span>
  </div>
  <div class="col-line" style="left:583px"></div>

  <h5 style="left:625px;width:223px">Newsletter Signup</h5>
  <p class="news-text">Lorem ipsum dolor sit consetuer adipiscing elit sed diam.</p>
  <div class="news-input">Email Address</div>
  <div class="news-btn">SUBSCRIBE</div>
  <div class="col-line" style="left:885px"></div>

  <div class="foot-brand">The<br>Brightledger Group</div>
  <div class="social"><span></span><span></span><span></span><span></span></div>
</footer>
<div class="abs copyright">Copyright © 2016 - Brightledgergroup.com | All rights reserved.</div>

</body>
</html>
```